Values Statement poster template

We want to develop a poster template for our company policies and statements which promote our company values in our workplaces.
These documents are important in showing our clients, suppliers and employees who we are and what we stand for.
The graphic design will incorporate our company logo, and be bright, uplifting and inspiring, developing a graphic theme that we can utilise for other company documents. The design will graphically illustrate and support our values statement, with colour and modern design.
This values poster will be the first in a series of documents using the same theme.The format will be a4 and a3 portrait
We are an environmental service business specialising in rehabilitation and revegetation

Target Market(s)

Tier one clients in industry, Mining, Construction and agriculture

Other font styles liked:
• calibri

Requirements
Must have
• Professional , high end feel, able to read clearly on a poster
Nice to have
• graphic design elements, symbols, etc which support the message, that can be carried through to various documents such as quality, environmental, safety policies
A bright theme which ties in with our logo colours.

```html
<!DOCTYPE html>
<html lang="en">
<head>
<meta charset="utf-8">
<title>Our Values – Verdanta</title>
<link href="https://fonts.googleapis.com/css2?family=Montserrat:wght@800&family=Oxygen:wght@400;700&display=swap" rel="stylesheet">
<style>
  :root{
    --orange:#ea6a1f;
    --orange-dark:#d4561a;
    --teal:#14a8c6;
    --teal-dark:#0f8fb0;
    --lime:#7cbb2c;
    --lime-dark:#66a324;
    --forest:#0f6a36;
    --forest-dark:#0b562b;
    --ink:#1f2326;
    --paper:#eef1f4;
    --accent-bar:#1aa3c9;
  }
  *{margin:0;padding:0;box-sizing:border-box}
  html,body{width:876px;height:1200px;overflow:hidden;background:#fff}
  .poster{
    position:relative;width:876px;height:1200px;overflow:hidden;
    background:linear-gradient(180deg,#f4f6f8 0%,#eceff2 55%,#e6eaed 100%);
    font-family:"Oxygen",sans-serif;color:var(--ink);
  }
  .photo-panel{
    position:absolute;left:0;top:0;width:295px;height:1200px;
    background:
      radial-gradient(ellipse 70% 30% at 60% 42%,rgba(110,150,70,.85) 0%,rgba(110,150,70,0) 70%),
      radial-gradient(ellipse 90% 25% at 40% 25%,rgba(230,236,240,.8) 0%,rgba(230,236,240,0) 70%),
      linear-gradient(180deg,#5d6f86 0%,#7f8fa2 14%,#6f7d70 32%,#4b5a3c 46%,#4a4635 60%,#3d3a2f 75%,#4f5a66 90%,#5e6a78 100%);
  }
  .title{
    position:absolute;right:calc(876px - 276px);top:50px;
    font-family:"Montserrat",sans-serif;font-weight:800;color:#fff;
    font-size:58px;line-height:56px;text-align:right;letter-spacing:.5px;
  }
  .title-rule{position:absolute;left:288px;top:54px;width:4px;height:108px;background:var(--accent-bar)}
  .brand{
    position:absolute;right:28px;top:36px;display:flex;align-items:center;gap:10px;
  }
  .brand-dot{width:30px;height:30px;border-radius:50%;background:var(--orange)}
  .brand-name{font-weight:700;font-size:38px;color:var(--forest);letter-spacing:-.5px}
  .tagline{
    position:absolute;left:311px;top:124px;width:540px;
    font-size:19px;line-height:25px;color:#333a3f;
  }
  .badge{
    position:absolute;left:231px;width:130px;height:130px;border-radius:50%;
    background:#fff;box-shadow:0 3px 10px rgba(0,0,0,.22);
    display:flex;align-items:center;justify-content:center;
  }
  .badge-core{width:112px;height:112px;border-radius:50%;display:flex;align-items:center;justify-content:center}
  .badge-core svg{width:70px;height:70px;fill:none;stroke:#fff;stroke-width:2.2;stroke-linecap:round;stroke-linejoin:round}
  .is-orange{background:linear-gradient(135deg,var(--orange) 50%,var(--orange-dark) 50%)}
  .is-teal{background:linear-gradient(135deg,var(--teal) 50%,var(--teal-dark) 50%)}
  .is-lime{background:linear-gradient(135deg,var(--lime) 50%,var(--lime-dark) 50%)}
  .is-forest{background:linear-gradient(135deg,var(--forest) 50%,var(--forest-dark) 50%)}
  .value{position:absolute;left:388px;width:470px;font-size:12.3px;line-height:14.4px}
  .value h2{font-weight:700;font-size:18.5px;line-height:20px;letter-spacing:.1px;text-transform:uppercase}
  .value p{margin:0}
  .value ul{list-style:none}
  .value li::before{content:"• "}
  .c-orange{color:var(--orange)}
  .c-teal{color:var(--teal)}
  .c-lime{color:var(--lime)}
  .c-forest{color:var(--forest)}
</style>
</head>
<body>
<div class="poster">
  <div class="photo-panel" role="img" aria-label="Photo of a young seedling growing in soil under a glass dome"></div>
  <h1 class="title">OUR<br>VALUES</h1>
  <div class="title-rule"></div>

  <div class="brand"><span class="brand-dot"></span><span class="brand-name">Verdanta</span></div>
  <p class="tagline">These are the things we value most, they define the way we do business</p>

  <!-- badges -->
  <div class="badge" style="top:198px"><div class="badge-core is-orange">
    <svg viewBox="0 0 70 70"><path d="M6 28l12-10 10 4 8-4 10 2"/><path d="M64 28L52 18"/><path d="M18 22l-8 14 16 16 6-2 6 4 12-8 10-8-6-12"/><path d="M26 40l6 6M32 36l8 8M38 32l8 8"/><path d="M10 14l6 4M60 14l-6 4"/></svg>
  </div></div>
  <div class="badge" style="top:341px"><div class="badge-core is-teal">
    <svg viewBox="0 0 70 70"><circle cx="35" cy="35" r="18"/><path d="M24 26c4 0 6 3 5 6s3 5 1 8M40 20c-2 4 2 6 6 6M38 46c2-4 6-4 8-2"/><path d="M12 30a24 24 0 0 1 40-14M58 40a24 24 0 0 1-40 14"/><path d="M52 10v6h-6M18 60v-6h6"/></svg>
  </div></div>
  <div class="badge" style="top:484px"><div class="badge-core is-lime">
    <svg viewBox="0 0 70 70"><rect x="26" y="34" width="18" height="28"/><rect x="8" y="44" width="16" height="18"/><rect x="46" y="40" width="16" height="22"/><path d="M31 30v-8h8v8M33 22l4-14"/><path d="M12 40v-6h8v6M50 36v-6h8v6"/></svg>
  </div></div>
  <div class="badge" style="top:627px"><div class="badge-core is-forest">
    <svg viewBox="0 0 70 70"><path d="M35 6l22 8v18c0 14-10 24-22 30C23 56 13 46 13 32V14z"/><path d="M35 12l16 6v14c0 10-7 18-16 23-9-5-16-13-16-23V18z"/><circle cx="35" cy="28" r="5"/><path d="M25 46c1-6 5-9 10-9s9 3 10 9"/></svg>
  </div></div>
  <div class="badge" style="top:770px"><div class="badge-core is-orange">
    <svg viewBox="0 0 70 70"><path d="M12 30a23 23 0 0 1 46 0"/><path d="M35 7v23M20 12c-4 6-4 12-4 18M50 12c4 6 4 12 4 18M14 20h42"/><circle cx="20" cy="40" r="4"/><circle cx="35" cy="40" r="4"/><circle cx="50" cy="40" r="4"/><path d="M13 60V50h14v10M28 60V50h14v10M43 60V50h14v10"/></svg>
  </div></div>
  <div class="badge" style="top:913px"><div class="badge-core is-teal">
    <svg viewBox="0 0 70 70"><rect x="10" y="10" width="50" height="50" rx="3"/><path d="M35 10v10a4 4 0 0 1 0 8v7H25a4 4 0 0 0-8 0H10M35 35h10a4 4 0 0 1 8 0h7M35 35v8a4 4 0 0 0 0 8v9"/></svg>
  </div></div>
  <div class="badge" style="top:1056px"><div class="badge-core is-lime">
    <svg viewBox="0 0 70 70"><circle cx="20" cy="24" r="7"/><circle cx="50" cy="24" r="7"/><path d="M8 54V44c0-6 5-10 12-10s12 4 12 10v10M38 54V44c0-6 5-10 12-10s12 4 12 10v10"/><path d="M24 60h22M28 57l-4 3 4 3M42 57l4 3-4 3"/></svg>
  </div></div>

  <!-- values -->
  <section class="value" style="top:206px">
    <h2 class="c-orange">We value our people above everything else</h2>
    <p>We demonstrate this by:</p>
    <ul>
      <li>Providing safe, positive, enjoyable workplaces where everyone feels valued and respected</li>
      <li>Providing Careers, not Jobs, we grow together</li>
      <li>Encouraging inclusion, participation and collaboration</li>
      <li>Recognising and rewarding contribution and excellence</li>
      <li>Supporting our people through tough times</li>
    </ul>
  </section>

  <section class="value" style="top:378px">
    <h2 class="c-teal">We do good things for the planet</h2>
    <p>Our products are helping revegetate Australia, which we are tremendously proud of.</p>
    <p>We minimise our environmental impact in everything we do.</p>
  </section>

  <section class="value" style="top:471px">
    <h2 class="c-lime">We set the standard</h2>
    <ul>
      <li>We are uncompromising on quality</li>
      <li>We are the best at what we do, and we do what we are best at</li>
      <li>We are always improving</li>
      <li>We are pioneering</li>
    </ul>
  </section>

  <section class="value" style="top:578px">
    <h2 class="c-forest">Our workplaces are safe</h2>
    <p>There is nothing more important to us than our people going home healthy and safe every<br>day. We won’t accept anything less. We believe safety is a management choice.</p>
    <p>By providing safe work systems, and education we achieve our daily goal of Zero Harm. At Verdanta</p>
    <p>We:</p>
    <ul>
      <li>Take the time to make our work areas safe, whatever it takes</li>
      <li>Don’t accept shortcuts</li>
      <li>Look out for each other</li>
      <li>Investigate our incidents and learn from them, we won’t accept repeats</li>
      <li>Are constantly looking for ways to improve the safety of our workplaces.</li>
      <li>Think safe, work safer, go home safe!</li>
    </ul>
  </section>

  <section class="value" style="top:814px">
    <h2 class="c-orange">We are proud of who we are</h2>
    <p>Our reputation means the world to us.</p>
    <p>We:</p>
    <ul>
      <li>Treat everyone with respect and we expect it in return</li>
      <li>Follow the rules</li>
      <li>Do what we say we will do</li>
      <li>Own our mistakes and we fix them</li>
      <li>Are trustworthy and transparent</li>
    </ul>
  </section>

  <section class="value" style="top:964px">
    <h2 class="c-teal">We succeed together</h2>
    <p>We believe in win-win relationships. When our business is profitable everyone benefits, our owners, employees, clients and the community. At Verdanta</p>
    <p>We:</p>
    <ul>
      <li>Work as a team, we get it done together</li>
      <li>We treat our suppliers and subcontractors like they are part of the team.</li>
      <li>Are building on our success, and growing together</li>
      <li>Choose to work with employees, customers and suppliers who fit our values</li>
    </ul>
  </section>

  <section class="value" style="top:1130px">
    <h2 class="c-lime">We give back</h2>
    <p style="margin-top:2px;line-height:16px">We appreciate our success and we give back by supporting our community, and those less fortunate.</p>
  </section>
</div>
</body>
</html>
```